Copper and Slate Mist NZ new website!

We are a new online vaping retailer and are looking for an awesome sleek website. We are going to be selling a variety of vaping products and gear. Our logo has just been developed and we would like to keep the website in line with the black, tan a white theme. We would like to trying watermarking or imposing the rottie into the background of the website on the home page, with the page being black and you can see the tan and white colours only.

Coding

Coded - Design and coding required

Number of Pages Required

2 page

Font styles to use
Serif
Sans Serif
Decorative

Requirements
Must have
• A home page and a standard page for products
• Stay in line with the colours in the logo

```html
<!DOCTYPE html>
<html lang="en">
<head>
<meta charset="utf-8">
<title>Copper and Slate Mist NZ</title>
<link rel="stylesheet" href="https://fonts.googleapis.com/css2?family=Montserrat:wght@400;500;600;700&family=Barlow:wght@400;500;600;700&family=Barlow+Condensed:wght@400;500;600&display=swap">
<style>
:root{
  --copper:#b8721e;
  --copper-light:#e2a33f;
  --ink:#17101a;
  --ink-2:#1f1620;
  --white:#ffffff;
  --grey-bg:#f1f1f1;
  --text:#222;
  --muted:#8a8a8a;
  --star:#f0b323;
}
*{box-sizing:border-box;margin:0;padding:0}
html,body{width:1200px;height:3279px;overflow:hidden}
body{position:relative;font-family:"Montserrat",sans-serif;color:var(--text);background:var(--white)}
.abs{position:absolute}
section,header,footer{position:absolute;left:0;width:1200px}

/* top bar */
.topbar{top:0;height:46px;background:var(--copper);color:var(--ink);font-size:17px;font-weight:500;display:flex;align-items:center;justify-content:center;gap:12px}

/* nav */
.nav{top:46px;height:94px;background:var(--ink);color:var(--white);z-index:5}
.nav .links{position:absolute;top:0;height:94px;display:flex;align-items:center;gap:26px;font-family:"Barlow",sans-serif;font-weight:600;font-size:15px;letter-spacing:.5px}
.nav .links .active{color:var(--copper-light)}
.icon-btn{position:absolute;top:23px;width:48px;height:48px;border-radius:50%;background:#3a3238;display:flex;align-items:center;justify-content:center}
.brand{position:absolute;left:530px;top:-2px;width:140px;height:140px;border-radius:50%;background:var(--ink);border:4px solid var(--copper);display:flex;align-items:center;justify-content:center;text-align:center;font-family:"Barlow",sans-serif;font-weight:700;font-size:17px;line-height:1.15;color:var(--copper-light);padding:14px}

/* hero */
.hero{top:140px;height:658px;background:radial-gradient(ellipse at 30% 55%,#cfcfcf 0%,#8d8d8d 40%,#3c3c3c 100%);color:var(--white);text-align:center}
.hero h1{position:absolute;top:245px;width:100%;font-family:"Montserrat",sans-serif;font-weight:700;font-size:46px}
.hero p{position:absolute;top:303px;width:100%;font-size:22px}
.btn-outline{display:inline-block;border:2px solid var(--copper);color:var(--white);font-family:"Barlow",sans-serif;font-weight:600;font-size:14px;letter-spacing:.5px;padding:10px 30px}
.hero .btn-outline{position:absolute;top:360px;left:526px;background:rgba(0,0,0,.25)}
.hero .arrow{position:absolute;top:318px}

/* categories */
.cats{top:798px;height:562px}
.cat{position:absolute;width:600px;height:281px;display:flex;align-items:center;justify-content:center;font-family:"Barlow",sans-serif;font-weight:600;font-size:30px;letter-spacing:3px;color:var(--white)}
.cat.kits{left:0;top:0;background:linear-gradient(135deg,#6d6e6f,#2f3033)}
.cat.devices{left:600px;top:0;background:linear-gradient(135deg,#4a4a4c,#1e1e20)}
.cat.juices{left:0;top:281px;background:linear-gradient(135deg,#5c4a38,#2d2826)}
.cat.accessories{left:600px;top:281px;background:linear-gradient(135deg,#3c4250,#1d2330)}
.diamond{position:absolute;left:532px;top:212px;width:136px;height:136px}
.diamond span{position:absolute;inset:0;display:flex;align-items:center;justify-content:center;font-family:"Barlow",sans-serif;font-weight:600;font-size:15px;color:var(--ink)}

/* featured */
.featured{top:1360px;height:531px}
.featured h2{position:absolute;left:46px;top:55px;font-size:29px;font-weight:600;color:#1a1a1a}
.tabs{position:absolute;left:620px;top:50px;display:flex;gap:20px}
.tab{width:166px;height:44px;border-radius:22px;border:2px solid #f0c89a;display:flex;align-items:center;justify-content:center;font-family:"Barlow",sans-serif;font-weight:600;font-size:14px;letter-spacing:.5px;color:#333}
.tab.active{background:var(--copper);border-color:var(--copper);color:var(--white)}
.product{position:absolute;top:140px;width:250px;text-align:center}
.product .thumb{height:250px;background:var(--grey-bg);display:flex;align-items:center;justify-content:center}
.product.hover .thumb{background:var(--white);box-shadow:0 4px 18px rgba(0,0,0,.12)}
.product .stars{margin-top:20px;color:var(--star);font-size:12px;letter-spacing:3px}
.product .name{margin-top:6px;font-size:14px;font-weight:500}
.product .price{margin-top:4px;font-size:15px;font-weight:600;color:var(--copper)}
.quick{position:absolute;right:10px;top:14px;display:flex;flex-direction:column;gap:12px}
.quick i{width:30px;height:30px;border-radius:50%;border:1.5px solid var(--copper-light);display:block}
.slide-arrow{position:absolute;top:238px;width:42px;height:42px;border-radius:50%;background:var(--white);box-shadow:0 2px 8px rgba(0,0,0,.1);display:flex;align-items:center;justify-content:center}

/* welcome */
.welcome{top:1891px;height:529px;background:var(--ink)}
.welcome .photo{position:absolute;left:0;top:0;width:601px;height:529px;background:linear-gradient(160deg,#8a7a62 0%,#5a4a36 50%,#2d241c 100%)}
.welcome .copy{position:absolute;left:648px;top:90px;width:506px;color:var(--white);text-align:center}
.welcome .eyebrow{font-size:16px}
.welcome h2{font-size:28px;font-weight:600;margin-top:8px}
.welcome .body{margin-top:22px;font-size:13.5px;line-height:22.5px;text-align:justify}
.welcome .btn-outline{margin-top:40px}

/* features */
.features{top:2420px;height:282px}
.feature{position:absolute;top:70px;width:230px;text-align:center}
.feature .ring{width:74px;height:74px;margin:0 auto;border-radius:50%;border:2px solid var(--copper);display:flex;align-items:center;justify-content:center}
.feature h3{margin-top:22px;font-family:"Barlow",sans-serif;font-weight:600;font-size:15px}
.feature p{margin-top:6px;font-size:13px;color:var(--muted);line-height:22px}

/* newsletter */
.newsletter{top:2702px;height:140px;background:var(--copper);color:var(--white)}
.newsletter h2{position:absolute;left:46px;top:40px;font-size:30px;font-weight:600}
.newsletter p{position:absolute;left:46px;top:80px;font-size:13px}
.signup{position:absolute;left:621px;top:46px;width:533px;height:48px;border-radius:24px;background:var(--white);display:flex;align-items:center;overflow:hidden}
.signup span{flex:1;padding-left:30px;font-size:13px;color:#777}
.signup b{width:160px;height:48px;background:var(--copper-light);color:var(--ink);display:flex;align-items:center;justify-content:center;font-family:"Barlow",sans-serif;font-weight:700;font-size:15px;border-radius:24px}

/* footer */
.footer{top:2842px;height:437px;background:var(--ink);color:#cfcfcf}
.footer .brand-mark{position:absolute;left:42px;top:60px;width:144px;height:144px;border-radius:50%;border:3px solid #6a6a6a;display:flex;align-items:center;justify-content:center;text-align:center;font-family:"Barlow",sans-serif;font-weight:700;font-size:17px;line-height:1.2;color:#bdbdbd;padding:18px}
.fcol{position:absolute;top:70px}
.fcol h4{font-family:"Barlow",sans-serif;font-weight:600;font-size:15px;color:var(--white)}
.fcol ul{list-style:none;margin-top:12px}
.fcol li{font-family:"Barlow",sans-serif;font-size:12.5px;line-height:28.3px}
.phone{font-family:"Barlow Condensed",sans-serif;font-size:23px;color:var(--white);margin-top:10px}
.fcol .small{font-family:"Barlow",sans-serif;font-size:12.5px;line-height:22px}
.rule{position:absolute;left:46px;right:46px;top:362px;height:1px;background:#2e2630}
.copyright{position:absolute;left:46px;top:392px;font-family:"Barlow",sans-serif;font-size:12px}
.pay{position:absolute;left:618px;top:390px;display:flex;gap:10px}
.pay i{width:26px;height:17px;border:1.5px solid #9a9a9a;border-radius:3px;display:block}
.social{position:absolute;left:905px;top:391px;display:flex;gap:10px}
.social i{width:15px;height:15px;border-radius:50%;background:#9a9a9a;display:block}
</style>
</head>
<body>

<div class="topbar">
  <svg width="24" height="18" viewBox="0 0 24 18" fill="none" stroke="#17101a" stroke-width="1.8"><rect x="1" y="2" width="14" height="10"/><path d="M15 5h4l3 4v3h-7"/><circle cx="6" cy="14" r="2"/><circle cx="18" cy="14" r="2"/></svg>
  Free Express Courier within NZ for orders over $50!
</div>

<header class="nav">
  <div class="icon-btn" style="left:22px">
    <svg width="18" height="18" viewBox="0 0 18 18" fill="none" stroke="#fff" stroke-width="2"><circle cx="7.5" cy="7.5" r="5.5"/><path d="M12 12l5 5"/></svg>
  </div>
  <nav class="links" style="left:92px">
    <span class="active">HOME</span><span>PRODUCTS</span><span>ACCESSORIES</span><span>VAPING INFO</span>
  </nav>
  <div class="brand">Copper and Slate Mist NZ</div>
  <nav class="links" style="left:724px">
    <span>ABOUT</span><span>CONTACT</span><span>CALL. 022 - 4410 - 582</span>
  </nav>
  <div class="icon-btn" style="left:1071px">
    <svg width="18" height="18" viewBox="0 0 18 18" fill="none" stroke="#fff" stroke-width="1.8"><circle cx="9" cy="6" r="4"/><path d="M2 17c0-4 3-6 7-6s7 2 7 6"/></svg>
  </div>
  <div class="icon-btn" style="left:1128px">
    <svg width="20" height="18" viewBox="0 0 20 18" fill="none" stroke="#fff" stroke-width="1.8"><path d="M1 1h3l2 11h11l2-8H5"/><circle cx="8" cy="16" r="1.3"/><circle cx="16" cy="16" r="1.3"/></svg>
  </div>
</header>

<section class="hero" role="img" aria-label="Black and white photo of a man exhaling vapour while holding a vape device">
  <svg class="arrow" style="left:36px" width="26" height="20" viewBox="0 0 26 20" fill="none" stroke="#fff" stroke-width="2"><path d="M10 2L2 10l8 8M2 10h22"/></svg>
  <h1>Copper and Slate Mist NZ</h1>
  <p>Your 1 stop Shop for the latest and gretest vape gear</p>
  <span class="btn-outline">SHOP NOW</span>
  <svg class="arrow" style="left:1138px" width="26" height="20" viewBox="0 0 26 20" fill="none" stroke="#fff" stroke-width="2"><path d="M16 2l8 8-8 8M24 10H2"/></svg>
</section>

<section class="cats">
  <div class="cat kits" role="img" aria-label="Photo of vape starter kits">STARTER KITS</div>
  <div class="cat devices" role="img" aria-label="Photo of a vape mod device">DEVICES</div>
  <div class="cat juices" role="img" aria-label="Photo of e-juice bottles">E-JUICES</div>
  <div class="cat accessories" role="img" aria-label="Photo of a vape tank accessory">ACCESSOIRES</div>
  <div class="diamond">
    <svg width="136" height="136" viewBox="0 0 136 136"><rect x="22" y="22" width="92" height="92" fill="#fff" transform="rotate(45 68 68)"/></svg>
    <span>SHOP!</span>
  </div>
</section>

<section class="featured">
  <h2>Featured Products</h2>
  <div class="tabs">
    <div class="tab active">NEW ARRIVALS</div>
    <div class="tab">BEST SELLER</div>
    <div class="tab">SPECIAL OFFER</div>
  </div>

  <div class="slide-arrow" style="left:26px">
    <svg width="16" height="14" viewBox="0 0 16 14" fill="none" stroke="#c9a06a" stroke-width="1.8"><path d="M7 1L1 7l6 6M1 7h14"/></svg>
  </div>

  <div class="product" style="left:46px">
    <div class="thumb" role="img" aria-label="Silver box mod product photo"><div style="width:64px;height:120px;background:linear-gradient(90deg,#aaa,#555);border-radius:6px"></div></div>
    <div class="stars">★★★★★</div>
    <div class="name">Lorem ipsum dolor sit amet</div>
    <div class="price">$23.90</div>
  </div>
  <div class="product hover" style="left:332px">
    <div class="thumb" role="img" aria-label="Grey vape mod product photo"><div style="width:62px;height:118px;background:linear-gradient(90deg,#888,#444);border-radius:5px"></div></div>
    <div class="quick"><i></i><i></i><i></i></div>
    <div class="stars">★★★★★</div>
    <div class="name">Aenean sit amet lorem</div>
    <div class="price">$35.90</div>
  </div>
  <div class="product" style="left:619px">
    <div class="thumb" role="img" aria-label="Black vape kit with tank product photo"><div style="width:46px;height:130px;background:linear-gradient(90deg,#333,#111);border-radius:4px"></div></div>
    <div class="stars">★★★★★</div>
    <div class="name">Donec ornare tempus est</div>
    <div class="price">$29.00</div>
  </div>
  <div class="product" style="left:905px">
    <div class="thumb" role="img" aria-label="White and black box mod product photo"><div style="width:44px;height:110px;background:linear-gradient(90deg,#eee,#222);border-radius:6px"></div></div>
    <div class="stars">★★★★★</div>
    <div class="name">Finibus ut ullamcorper quis</div>
    <div class="price">$14.00</div>
  </div>

  <div class="slide-arrow" style="left:1132px">
    <svg width="16" height="14" viewBox="0 0 16 14" fill="none" stroke="#c9a06a" stroke-width="1.8"><path d="M9 1l6 6-6 6M15 7H1"/></svg>
  </div>
</section>

<section class="welcome">
  <div class="photo" role="img" aria-label="Photo of two rottweiler dogs resting on a wooden deck"></div>
  <div class="copy">
    <div class="eyebrow">Welcome to</div>
    <h2>Copper and Slate Mist NZ.</h2>
    <p class="body">Lorem ipsum dolor sit amet, consectetur adipiscing elit, sed do eiusmod tempor incididunt ut labore et dolore magna aliqua. Ut enim ad minim veniam, quis nostrud exercitation ullamco laboris nisi ut aliquip ex ea commodo consequat. Duis aute irure dolor in reprehenderit in voluptate velit esse cillum dolore eu fugiat nulla pariatur. Excepteur sint occaecat cupidatat non proident. Sed ut perspiciatis unde omnis iste natus error sit voluptatem accusantium doloremque laudantium, totam rem aperiam, eaque ipsa quae ab illo inventore veritatis et quasi architecto beatae.</p>
    <span class="btn-outline">FIND OUT MORE</span>
  </div>
</section>

<section class="features">
  <div class="feature" style="left:55px">
    <div class="ring"><svg width="30" height="22" viewBox="0 0 24 18" fill="none" stroke="#b8721e" stroke-width="1.6"><rect x="1" y="2" width="14" height="10"/><path d="M15 5h4l3 4v3h-7"/><circle cx="6" cy="14" r="2"/><circle cx="18" cy="14" r="2"/></svg></div>
    <h3>FREE SHIPPING</h3>
    <p>Lorem Ipsum has been the indus-<br>try's standard dummy.</p>
  </div>
  <div class="feature" style="left:342px">
    <div class="ring"><svg width="28" height="28" viewBox="0 0 24 24" fill="none" stroke="#b8721e" stroke-width="1.8"><path d="M3 14v-2a9 9 0 0118 0v2"/><rect x="2" y="14" width="5" height="7" rx="1"/><rect x="17" y="14" width="5" height="7" rx="1"/></svg></div>
    <h3>24/7 SUPPORT</h3>
    <p>Lorem Ipsum has been the indus-<br>try's standard dummy.</p>
  </div>
  <div class="feature" style="left:628px">
    <div class="ring"><svg width="28" height="28" viewBox="0 0 24 24" fill="none" stroke="#b8721e" stroke-width="1.8"><path d="M2 10h4v11H2zM6 10l5-8c2 0 3 1 2.5 3L13 9h7c1 0 2 1 1.7 2.2l-2 8c-.2.8-1 1.3-1.8 1.3H6"/></svg></div>
    <h3>WARRANTY</h3>
    <p>Lorem Ipsum has been the indus-<br>try's standard dummy.</p>
  </div>
  <div class="feature" style="left:915px">
    <div class="ring"><svg width="28" height="28" viewBox="0 0 24 24" fill="none" stroke="#b8721e" stroke-width="1.8"><path d="M13 2h9v9L11 22 2 13z"/><circle cx="17" cy="7" r="1.5"/></svg></div>
    <h3>GET DISCOUNT</h3>
    <p>Lorem Ipsum has been the indus-<br>try's standard dummy.</p>
  </div>
</section>

<section class="newsletter">
  <h2>Get $10 Off + Free Shipping*</h2>
  <p>Sign up and get an instant discount and exclusive access to future offers!</p>
  <div class="signup"><span>Enter your email ...</span><b>SIGN UP NOW!</b></div>
</section>

<footer class="footer">
  <div class="brand-mark">Copper and Slate Mist NZ</div>
  <div class="fcol" style="left:332px">
    <h4>Shop Categories</h4>
    <ul><li>Clearance Sale</li><li>Accessories</li><li>E-Liquid</li><li>MODs / APVs</li><li>Replacement Coils</li><li>Tanks &amp; RDAs</li><li>Starter Kits</li></ul>
  </div>
  <div class="fcol" style="left:619px">
    <h4>Quick Link</h4>
    <ul><li>About Us</li><li>FDA Age Verification</li><li>In Store Pickup / Shipping</li><li>Warranty &amp; Returns</li><li>Blog</li><li>Contact</li></ul>
  </div>
  <div class="fcol" style="left:905px">
    <h4>Contact Info</h4>
    <div class="phone">P. 021 - 5530 - 217</div>
    <div class="small">e. hello@copperslatemist.nz</div>
    <div class="small" style="margin-top:22px">48 Harbour Lane,<br>Kawau Bay,<br>Auckland</div>
  </div>
  <div class="rule"></div>
  <div class="copyright">Copyright © 2019 Copper and Slate Mist NZ. All Rights Reserved</div>
  <div class="pay" aria-label="Accepted payment methods"><i></i><i></i><i></i><i></i><i></i></div>
  <div class="social" aria-label="Social links"><i></i><i></i><i></i><i></i></div>
</footer>

</body>
</html>
```